Website and wholesale branding

We’re a new cafe looking to take our branding and business to the next level, we need a website built with the ability to add wholesale + retail products that can integrate with our p.o.s that’s easy to manage and looks professional. we need product labels, coffee packaging labels with product information branding.
Please see our current website www.tinmorrow.com.au

Target Market(s)

Locals in Geelong, coffee lovers, foodies, tourists, hospitality industry

Coding

Coded - Design and coding required

Number of Pages Required

1 page

Font styles to use
Serif

Colors
87d0c7
abd037

Requirements
Must have
• Business mission statement, information about the farms we support
Nice to have
• Venue photos, food pics

```html
<!DOCTYPE html>
<html lang="en">
<head>
<meta charset="utf-8">
<title>Tinmorrow – The Coffee</title>
<link href="https://fonts.googleapis.com/css2?family=Crimson+Pro:wght@400;600;700&family=Open+Sans:wght@400;600&display=swap" rel="stylesheet">
<style>
:root{
  --teal:#87d0c7;
  --lime:#abd037;
  --lime-deep:#9cc22c;
  --ink:#1b1b1b;
  --text:#333;
  --muted:#555;
  --shadow:#e4e4e4;
  --white:#fff;
  --dark:#231f1c;
}
*{margin:0;padding:0;box-sizing:border-box}
html,body{width:1200px;height:3934px;overflow:hidden;background:var(--white)}
body{font-family:"Open Sans",sans-serif;color:var(--text)}
h2{font-weight:400}
.page{position:relative;width:1200px;height:3934px;overflow:hidden}
.abs{position:absolute}

/* header */
.site-header{left:0;top:0;width:1200px;height:95px;background:var(--white);z-index:3}
.brand{left:143px;top:16px;display:flex;align-items:center;gap:14px}
.brand-dot{width:44px;height:44px;border-radius:50%;background:var(--ink)}
.brand-name{font-family:"Crimson Pro",serif;font-weight:700;font-size:52px;color:var(--ink);line-height:1}
.header-phone{right:145px;top:12px;font-family:"Crimson Pro",serif;font-size:25px;color:var(--ink);display:flex;align-items:center;gap:8px}
.main-nav{right:145px;top:60px;display:flex;gap:32px;font-family:"Crimson Pro",serif;font-size:17px;color:var(--ink)}
.main-nav .active{color:var(--lime-deep)}

/* hero */
.hero{left:0;top:95px;width:1200px;height:620px}
.hero-photo{position:absolute;inset:0;background:linear-gradient(100deg,#7fa9cf 0%,#c9d3dc 22%,#f2f2f0 42%,#e9ebee 60%,#9bb9d8 78%,#6d8fb5 100%)}
.hero-shade{position:absolute;inset:0;background:linear-gradient(180deg,rgba(0,0,0,0) 45%,rgba(90,88,84,.55) 100%)}
.hero-curve{position:absolute;left:0;bottom:0}
.hero-badge{left:144px;top:50px;width:436px;height:436px;border-radius:50%;background:#151515;text-align:center;color:var(--white)}
.hero-kicker{font-family:"Crimson Pro",serif;font-size:34px;margin-top:102px;letter-spacing:.3px}
.hero-title{font-family:"Crimson Pro",serif;font-weight:700;font-size:47px;line-height:56px;color:var(--lime);margin-top:6px}
.hero-dots{display:flex;justify-content:center;gap:20px;margin-top:28px}
.hero-dots span{width:11px;height:11px;border-radius:50%;background:#6a6a6a}
.hero-dots span.on{background:var(--white)}

/* feature blocks */
.shadow-box{background:var(--shadow)}
.photo{position:absolute}
.block-title{font-family:"Crimson Pro",serif;font-size:35px;color:var(--ink)}
.block-text{font-size:16px;line-height:33.6px;color:var(--muted);width:412px;margin-top:14px}
.btn{display:inline-block;background:var(--teal);color:#234;font-family:"Crimson Pro",serif;font-size:18px;padding:0 22px;height:56px;line-height:56px;margin-top:30px}

/* menu band */
.menu-band{left:0;top:1438px;width:1200px;height:544px;background:linear-gradient(160deg,#2f2620 0%,#5a4636 35%,#4b3b2e 60%,#2a231d 100%)}
.menu-title{position:absolute;left:0;width:1200px;top:64px;text-align:center;font-family:"Crimson Pro",serif;font-size:33px;color:var(--white)}
.menu-card{position:absolute;top:124px;width:219px;height:264px;background:var(--white);padding:7px}
.menu-card .thumb{width:205px;height:194px}
.menu-card p{font-family:"Crimson Pro",serif;font-size:16px;line-height:20px;text-align:center;color:var(--ink);margin-top:12px}
.btn-ghost{position:absolute;left:531px;top:414px;width:136px;height:54px;border:1.5px solid rgba(255,255,255,.75);color:var(--white);font-family:"Crimson Pro",serif;font-size:17px;text-align:center;line-height:51px}

/* location */
.map{left:0;top:3360px;width:1200px;height:420px;background:linear-gradient(120deg,#e9ece4 0%,#f3ecd8 30%,#e6ebe3 55%,#efe8d6 80%,#e4e9e2 100%)}
.contact-bar{left:0;top:3360px;width:1200px;height:62px;background:rgba(171,208,55,.92);display:flex;justify-content:center;align-items:center;gap:20px;font-size:20px;color:var(--ink)}
.contact-bar .item{display:flex;align-items:center;gap:8px}

/* footer */
.footer-curve{left:0;top:3720px}
.site-footer{left:0;top:3800px;width:1200px;height:134px;background:var(--dark)}
.footer-nav{position:absolute;left:143px;top:44px;display:flex;gap:10px;font-size:11.5px;color:#ddd}
.copyright{position:absolute;left:143px;top:76px;font-size:11.5px;color:#ccc}
.social{position:absolute;left:980px;top:58px;display:flex;gap:30px}
.social span{width:20px;height:20px;border-radius:50%;background:#d8d8d8}
</style>
</head>
<body>
<div class="page">

  <header class="site-header abs">
    <div class="brand abs">
      <span class="brand-dot"></span>
      <span class="brand-name">tinmorrow</span>
    </div>
    <div class="header-phone abs">
      <svg width="18" height="18" viewBox="0 0 24 24"><path fill="#1b1b1b" d="M6.6 10.8a15 15 0 0 0 6.6 6.6l2.2-2.2c.3-.3.7-.4 1-.2 1.1.4 2.3.6 3.6.6.6 0 1 .4 1 1V20c0 .6-.4 1-1 1A17 17 0 0 1 3 4c0-.6.4-1 1-1h3.5c.6 0 1 .4 1 1 0 1.3.2 2.5.6 3.6.1.3 0 .7-.2 1z"/></svg>
      (03) 5210 4187
    </div>
    <nav class="main-nav abs">
      <span class="active">The Coffee</span><span>Menu</span><span>Eco Lodge</span><span>About</span><span>Location</span><span>Contact</span>
    </nav>
  </header>

  <section class="hero abs">
    <div class="hero-photo" role="img" aria-label="Street corner view of the white café building with striped awning"></div>
    <div class="hero-shade"></div>
    <svg class="hero-curve" width="1200" height="120" viewBox="0 0 1200 120" preserveAspectRatio="none">
      <path d="M0 20 Q600 150 1200 20 L1200 120 L0 120Z" fill="#fff"/>
      <path d="M0 20 Q600 150 1200 20 Q600 118 0 20Z" fill="#abd037"/>
    </svg>
    <div class="hero-badge abs">
      <div class="hero-kicker">FIRST CROP COFFEE</div>
      <div class="hero-title">NICARAGUA LAS<br>BRUMAS<br>–MONTE OSCURO</div>
      <div class="hero-dots"><span class="on"></span><span></span><span></span><span></span></div>
    </div>
  </section>

  <!-- welcome -->
  <div class="shadow-box abs" style="left:143px;top:817px;width:433px;height:540px"></div>
  <div class="photo" role="img" aria-label="Café interior with long timber table, shelving and brick wall" style="left:168px;top:789px;width:432px;height:544px;background:linear-gradient(170deg,#4a2a1a 0%,#7a4328 30%,#a8663a 60%,#d09a64 100%)"></div>
  <div class="abs" style="left:647px;top:852px">
    <h2 class="block-title">Welcome to Tinmorrow</h2>
    <p class="block-text">Vestibulum condimentum, risus posuere cursus, velit justo accumsan sem, lobortis aliquet metus dui eu libero. Pellentesque a imperdiet dolor, et auctor est. Fusce sollicitudin lorem et luctus volutpat. Proin plac erat dapibus gravida. In tristique tristique nulla eget hendrerit. Maecenas vel tortor accumsan quam varius imperdiet vel eget elit. Aenean facilisis tincidunt lectus, id dictum nisi luctus eget.</p>
    <span class="btn">READ MORE</span>
  </div>

  <!-- menu -->
  <section class="menu-band abs" role="img" aria-label="Café table with coffee and newspapers, darkened backdrop">
    <h2 class="menu-title">Our Menu Items</h2>
    <div class="menu-card" style="left:143px"><div class="thumb" style="background:linear-gradient(165deg,#2e2018,#6e4630 50%,#4f7a56)" role="img" aria-label="Latte with a pastry"></div><p>Etiam vel massa<br>elementum</p></div>
    <div class="menu-card" style="left:375px"><div class="thumb" style="background:linear-gradient(165deg,#7a2a22,#a86d3c 55%,#5a4030)" role="img" aria-label="Sourdough loaves on a rack"></div><p>Etiam mattis augue<br>vehicula odio</p></div>
    <div class="menu-card" style="left:607px"><div class="thumb" style="background:linear-gradient(165deg,#6a4228,#8a6040 50%,#3f7a5c)" role="img" aria-label="Breakfast bowls with coffee"></div><p>Cras sollicitudin<br>cursus dui</p></div>
    <div class="menu-card" style="left:839px"><div class="thumb" style="background:linear-gradient(165deg,#5e6a3a,#c99762 55%,#2f2f33)" role="img" aria-label="Filled baguette with chips"></div><p>Pellentesque convallis<br>molestie enim</p></div>
    <span class="btn-ghost">VIEW ALL</span>
  </section>

  <!-- coffee -->
  <div class="shadow-box abs" style="left:625px;top:2086px;width:430px;height:544px"></div>
  <div class="photo" role="img" aria-label="Farm worker turning organic compost in a timber shed" style="left:600px;top:2063px;width:432px;height:542px;background:linear-gradient(180deg,#d6d1c4 0%,#8c7a66 35%,#5a4130 65%,#3e2a1c 100%)"></div>
  <div class="abs" style="left:143px;top:2128px">
    <h2 class="block-title">The Coffee</h2>
    <p class="block-text">Las brumas has 12 separate lots, each lot is separated by varietal and unqiue in it's elevation, with the elevation ranging from 1200-1400masl. the lots are shade grown and the trees are fertilized with organic fertilizer made on the farm, las brumas is certified organic. the cherries are picked and then taken to the wet mill on the farm, where the coffee is processed using water from the mountain.</p>
    <span class="btn">READ MORE</span>
  </div>

  <!-- eco lodge -->
  <div class="shadow-box abs" style="left:143px;top:2735px;width:433px;height:543px"></div>
  <div class="photo" role="img" aria-label="Hillside eco village with red roofs among green trees" style="left:168px;top:2710px;width:432px;height:543px;background:linear-gradient(180deg,#9fbde0 0%,#e3e8ee 18%,#7b8f88 32%,#5f8a4e 48%,#9a4a3a 58%,#3f6a30 70%,#2f4a24 100%)"></div>
  <div class="abs" style="left:647px;top:2762px">
    <h2 class="block-title">Eco-Lodge</h2>
    <p class="block-text">Along with growing coffee, monte oscuro has developed into a completely self-sustaining eco village. there is a vegetable garden which provides vegetables for the restaurant, a farm of pigs, cows and chickens for meat and eggs. there is also a bakery and a cheese making factory. the power is generated by solar panels around the farm and on the roofs. Methane gas is produced for cooking by using the waste water from coffee processing.</p>
    <span class="btn">READ MORE</span>
  </div>

  <!-- location -->
  <div class="map abs" role="img" aria-label="Street map of central Geelong with the café location pinned"></div>
  <div class="contact-bar abs">
    <span class="item"><svg width="12" height="18" viewBox="0 0 12 18"><path d="M6 0a6 6 0 0 0-6 6c0 4.5 6 12 6 12s6-7.5 6-12a6 6 0 0 0-6-6zm0 8.5A2.5 2.5 0 1 1 6 3.5a2.5 2.5 0 0 1 0 5z" fill="#1b1b1b"/></svg>48 Harbour Lane, Geelong</span>
    <span>|</span>
    <span class="item"><svg width="16" height="16" viewBox="0 0 24 24"><path fill="#1b1b1b" d="M6.6 10.8a15 15 0 0 0 6.6 6.6l2.2-2.2c.3-.3.7-.4 1-.2 1.1.4 2.3.6 3.6.6.6 0 1 .4 1 1V20c0 .6-.4 1-1 1A17 17 0 0 1 3 4c0-.6.4-1 1-1h3.5c.6 0 1 .4 1 1 0 1.3.2 2.5.6 3.6.1.3 0 .7-.2 1z"/></svg>Phone: (03) 5210 4187</span>
    <span>|</span>
    <span class="item"><svg width="18" height="14" viewBox="0 0 18 14"><rect width="18" height="14" rx="1" fill="#1b1b1b"/><path d="M1 1l8 6 8-6" stroke="#abd037" stroke-width="1.5" fill="none"/></svg>Email: hello@tinmorrow.com.au</span>
  </div>

  <svg class="footer-curve abs" width="1200" height="82" viewBox="0 0 1200 82" preserveAspectRatio="none">
    <path d="M0 82 Q600 -40 1200 82Z" fill="#231f1c"/>
  </svg>
  <footer class="site-footer abs">
    <div class="footer-nav"><span>The Coffee</span><span>|</span><span>Menu</span><span>|</span><span>Eco Lodge</span><span>|</span><span>About</span><span>|</span><span>Location</span><span>|</span><span>Contact</span></div>
    <div class="copyright">Copyright © 2021 &nbsp; Tinmorrow. &nbsp; All rights reserved.</div>
    <div class="social"><span></span><span></span></div>
  </footer>

</div>
</body>
</html>
```